Brenmoor Group needs a business card

I would like the card to be simple but modern and elegant.
I like black and white.
or black and gold.
we are a private finance lender and also are involved in property and property developments.

please look at the business card photos i provided i would like B.G only one one side and all the other details on the other side use fonts that tie in with my theme.

Industry/Entity Type

Finance

Contact Information for Business Card

Brenmoor Group (B.G) Callum Brenmoor M: 0418396152 E: callumbren@quivomail.com

Font styles to use
Other font styles liked:
• Use fonts that would reflect our business

Colors
000000
ffffff

Requirements
Must have
• one side of details
• other side has either B.G or Brenmoor Group like in the photos provided

```html
<!DOCTYPE html>
<html lang="en">
<head>
<meta charset="utf-8">
<title>Brenmoor Group — Business Card</title>
<link rel="stylesheet" href="https://fonts.googleapis.com/css2?family=EB+Garamond:wght@400;500&family=Great+Vibes&display=swap">
<style>
  :root {
    --page: #ffffff;
    --card: #000000;
    --gold-deep: #8a5a1f;
    --gold: #c8913a;
    --gold-light: #f5d98a;
    --gold-text: #e2b766;
    --shadow: rgba(0, 0, 0, 0.45);
  }
  * { margin: 0; padding: 0; box-sizing: border-box; }
  html, body {
    width: 1200px;
    height: 848px;
    overflow: hidden;
    background: var(--page);
  }
  .canvas {
    position: relative;
    width: 1200px;
    height: 848px;
  }
  .card {
    position: absolute;
    width: 666px;
    height: 370px;
    background: var(--card);
    box-shadow: 3px 6px 10px var(--shadow);
  }
  .card--front { left: 81px; top: 28px; }
  .card--back  { left: 484px; top: 437px; }

  .holder-name {
    position: absolute;
    right: 372px;
    top: 118px;
    padding: 10px 20px 16px 28px;
    font-family: "Great Vibes", cursive;
    font-weight: 400;
    font-size: 56px;
    line-height: 52px;
    text-align: right;
    white-space: nowrap;
    background: linear-gradient(100deg, var(--gold-deep) 0%, var(--gold) 30%, var(--gold-light) 55%, var(--gold) 75%, var(--gold-deep) 100%);
    -webkit-background-clip: text;
    background-clip: text;
    color: transparent;
  }
  .holder-name span { display: block; }

  .divider {
    position: absolute;
    left: 302px;
    top: 76px;
    width: 2px;
    height: 222px;
    background: linear-gradient(180deg, transparent 0%, var(--gold) 25%, var(--gold-light) 55%, var(--gold) 80%, transparent 100%);
  }

  .contact {
    position: absolute;
    left: 325px;
    top: 170px;
    font-family: "EB Garamond", serif;
    font-size: 24px;
    line-height: 30px;
    color: var(--gold-text);
    list-style: none;
    white-space: nowrap;
  }

  .brand-name {
    position: absolute;
    left: 0;
    right: 0;
    top: 146px;
    text-align: center;
    font-family: "EB Garamond", serif;
    font-weight: 400;
    font-size: 58px;
    line-height: 66px;
    color: var(--gold);
  }
</style>
</head>
<body>
<main class="canvas">
  <section class="card card--front" aria-label="Business card front">
    <h1 class="holder-name"><span class="first">Callum</span><span class="last">Brenmoor</span></h1>
    <div class="divider"></div>
    <ul class="contact">
      <li class="contact__phone">0418396152</li>
      <li class="contact__email">callumbren@quivomail.com</li>
    </ul>
  </section>

  <section class="card card--back" aria-label="Business card back">
    <p class="brand-name">Brenmoor Group</p>
  </section>
</main>
</body>
</html>
```